Martin Hale / Tidemark General

I own a remodeling company as well as a real estate business. I'd like each side of the card to be dedicated that that one business. I would love to see designs that are creative and with out to much visual overload. Less might be more. For the remodeling side, I was thinking about the possibility that ONE OF THE CONCEPTS could have the image centered at the bottom of the card allowing the remaining three sides to have the rest of the text.... just a thought.

Target Market(s)

wealthy second homeowners. 55-80 years old.

Industry/Entity Type

Business

Font styles to use
Sans Serif
Script

Requirements
Should not have
• Space for address.

```html
<!DOCTYPE html>
<html lang="en">
<head>
<meta charset="utf-8">
<title>Tidemark General Contracting LLC</title>
<link rel="stylesheet" href="https://fonts.googleapis.com/css2?family=Open+Sans:wght@400;600;700&display=swap">
<style>
  :root {
    --brand-red: #e8432e;
    --brand-orange: #f5821f;
    --ink: #333333;
    --ink-soft: #4a4a4a;
    --paper: #f1f1f1;
    --white: #ffffff;
    --badge: #2b2b2b;
  }
  * { margin: 0; padding: 0; box-sizing: border-box; }
  html, body { width: 1200px; height: 800px; overflow: hidden; }
  body { font-family: "Open Sans", Arial, sans-serif; color: var(--ink); }

  .card {
    position: relative;
    width: 1200px;
    height: 800px;
    overflow: hidden;
    background: var(--paper);
  }
  .card__backdrop {
    position: absolute; inset: 0;
    background: linear-gradient(160deg, #e4e4e4 0%, #f7f7f7 45%, #ececec 100%);
  }

  .brand {
    position: absolute;
    top: 22px; left: 0; width: 100%;
    display: flex; flex-direction: column; align-items: center;
  }
  .brand__tagline {
    font-size: 22px; font-weight: 400; color: var(--ink);
    border-bottom: 2px solid var(--ink);
    padding-bottom: 2px; margin-left: 200px;
  }
  .brand__row { display: flex; align-items: center; gap: 16px; margin-top: 4px; }
  .brand__mark {
    width: 54px; height: 54px; border-radius: 50%;
    background: var(--brand-orange);
  }
  .brand__name {
    font-size: 66px; font-weight: 700; line-height: 1;
    color: var(--brand-red); letter-spacing: -1px;
  }
  .brand__legal {
    font-size: 24px; font-weight: 400; color: var(--ink);
    letter-spacing: 1px; margin-top: 8px;
  }

  .band-headline {
    position: absolute; top: 197px; left: 0; width: 100%; height: 53px;
    background: var(--brand-red);
    display: flex; align-items: center; justify-content: center;
    color: var(--white); font-size: 32px; font-weight: 700;
  }

  .showcase {
    position: absolute; top: 250px; left: 0; width: 100%; height: 278px;
    background: linear-gradient(100deg, #6b5340 0%, #a8866a 30%, #d8cbb6 50%, #8c6f55 70%, #5e4736 100%);
  }

  .band-services {
    position: absolute; top: 528px; left: 0; width: 100%; height: 75px;
    background: var(--brand-orange);
    color: var(--white); font-size: 28px; font-weight: 400;
    display: flex; flex-direction: column; align-items: center; justify-content: center;
    line-height: 1.2;
  }
  .band-services__sep { margin: 0 24px; }

  .contact {
    position: absolute; top: 606px; left: 0; width: 100%;
    text-align: center;
  }
  .contact__phone {
    font-size: 50px; font-weight: 700; color: var(--brand-red); line-height: 1.2;
  }
  .contact__person, .contact__web {
    font-size: 19px; color: var(--ink-soft); line-height: 1.3;
  }

  .payments {
    position: absolute; top: 660px; left: 34px;
    display: flex; gap: 14px;
  }
  .payments__card {
    width: 66px; height: 44px; border-radius: 3px;
    border: 1px solid #bbbbbb; background: var(--white);
  }
  .credentials {
    position: absolute; top: 720px; left: 39px;
    font-size: 24px; color: var(--ink-soft); line-height: 1.3;
  }

  .affiliations {
    position: absolute; top: 659px; left: 790px;
    display: flex; gap: 12px; align-items: flex-end;
  }
  .affiliations__badge { display: block; }
</style>
</head>
<body>
<div class="card">
  <div class="card__backdrop" role="img" aria-label="Faded interior photograph of a remodeled home as background"></div>

  <header class="brand">
    <p class="brand__tagline">The Art of Remodeling</p>
    <div class="brand__row">
      <span class="brand__mark"></span>
      <span class="brand__name">TIDEMARK</span>
    </div>
    <p class="brand__legal">GENERAL CONTRACTING LLC</p>
  </header>

  <div class="band-headline">Remodeling Homes &amp; Building Lasting Relationships Since 1995</div>

  <div class="showcase" role="img" aria-label="Photograph of a luxury living room with stacked stone columns, cream sofas and wood beams"></div>

  <div class="band-services">
    <p>All Phases of Residential Remodeling<span class="band-services__sep">|</span>Partial &amp; Large Scale Renovations</p>
    <p>Complimentary Design Services</p>
  </div>

  <section class="contact">
    <p class="contact__phone">(480) 555-0142</p>
    <p class="contact__person">Martin Hale, General Contractor</p>
    <p class="contact__web">www.MartinHaleAZ.com</p>
  </section>

  <div class="payments" aria-label="Accepted payment cards">
    <span class="payments__card"></span>
    <span class="payments__card"></span>
    <span class="payments__card"></span>
    <span class="payments__card"></span>
  </div>

  <div class="credentials">
    <p>Licensed | Bonded | Insured</p>
    <p>License # B418637</p>
  </div>

  <div class="affiliations" aria-label="Housing and listing affiliations">
    <svg class="affiliations__badge" width="110" height="118" viewBox="0 0 110 118">
      <rect x="4" y="4" width="102" height="110" fill="var(--badge)"/>
    </svg>
    <svg class="affiliations__badge" width="272" height="122" viewBox="0 0 272 122">
      <rect x="2" y="2" width="268" height="118" fill="none" stroke="var(--badge)" stroke-width="3"/>
      <rect x="18" y="14" width="92" height="94" fill="var(--badge)"/>
      <rect x="128" y="40" width="126" height="46" fill="var(--badge)"/>
    </svg>
  </div>
</div>
</body>
</html>
```